Brochure Design Project for Home Watch company

We are a new start up company in fast growing home watch industry. We provide services in Hawaii so the design needs to be reflect that. Our web site can give you overview of what we do - www.breezekeepcare.com. We will service clients that own second homes in Hawaii. These properties are not necessarily income producing properties for our clients. I'm looking for 2 or 4 page brochure which will be used to market our services to potential new clients. It needs to be high quality, modern with slight Hawaiian feel (we are based on Oahu). I'm not looking for a trifold type of brochure.

We are open to various colors based on what the designer might suggest but as you can see on our home page - the main picture of the home on our site has lots of red and white which we like as well as the "head" or dot above the "i" in our logo is red. I was not able to upload the file of the main house (purchased on snapmeadow) on here therefore I'll have to provide the original photo to the selected designer at the later time. For now I just uploaded the not purchased copy.

If you have other questions please do let me know. And lastly, I will be looking to create a business card and post card as well.

```html
<!DOCTYPE html>
<html lang="en">
<head>
<meta charset="utf-8">
<title>Breeze Keep Care – Brochure</title>
<link rel="stylesheet" href="https://fonts.googleapis.com/css2?family=Lato:ital,wght@0,400;0,700;0,900;1,400;1,700;1,900&family=Oswald:wght@500;600&display=swap">
<style>
  :root {
    --red: #e8333a;
    --red-dark: #b8141c;
    --black: #141414;
    --ink: #2b2b2b;
    --grey: #6d6d6d;
    --white: #ffffff;
    --stage: #e9e9e9;
    --sky: #5da7d9;
    --sea: #1f8fb8;
    --sand: #e8dcc2;
  }
  * { box-sizing: border-box; margin: 0; padding: 0; }
  html, body { width: 1098px; height: 1200px; overflow: hidden; }
  body { background: var(--stage); font-family: "Lato", sans-serif; color: var(--ink); position: relative; }

  .spread { position: absolute; left: 39px; width: 1020px; height: 560px; display: flex; box-shadow: 0 8px 24px rgba(0,0,0,.18); }
  .spread--outer { top: 30px; }
  .spread--inner { top: 610px; }
  .page { position: relative; width: 510px; height: 560px; overflow: hidden; background: var(--white); }
  .page > svg.page-art { position: absolute; inset: 0; width: 100%; height: 100%; }

  .heading { font-weight: 900; color: var(--red); font-size: 17px; }
  .body-copy { font-size: 9.5px; line-height: 1.4; color: var(--ink); }
  .subhead { font-weight: 900; font-style: italic; font-size: 12px; color: var(--red-dark); }

  /* Back cover */
  .about { position: absolute; left: 28px; top: 22px; width: 455px; }
  .about .heading { margin-bottom: 3px; }
  .about .body-copy { margin-bottom: 8px; }
  .contact { position: absolute; left: 120px; top: 440px; width: 240px; color: var(--white); text-align: center; font-size: 13px; font-weight: 700; line-height: 1.55; }
  .contact .line { display: flex; justify-content: center; align-items: center; gap: 6px; }
  .contact svg { width: 11px; height: 11px; }

  /* Front cover */
  .brand-badge { position: absolute; left: 330px; top: 215px; width: 140px; height: 140px; border-radius: 50%; background: var(--white); border: 3px solid var(--red); display: flex; flex-direction: column; align-items: center; justify-content: center; }
  .brand-badge .brand-name { font-weight: 900; font-size: 15px; color: var(--black); text-align: center; line-height: 1.15; }
  .brand-badge .brand-tag { font-size: 9px; color: var(--ink); margin-top: 6px; font-weight: 700; }
  .cover-title { position: absolute; right: 26px; top: 385px; text-align: right; }
  .cover-title .lead { font-family: "Lato", sans-serif; font-weight: 900; font-size: 30px; color: var(--red); }
  .cover-title .main { font-family: "Oswald", sans-serif; font-weight: 600; font-size: 26px; line-height: 1.1; color: var(--white); text-transform: uppercase; }

  /* Inner left */
  .intro { position: absolute; left: 28px; top: 26px; width: 460px; }
  .illustration { position: absolute; left: 60px; top: 92px; width: 300px; height: 180px; }
  .section-tab { position: absolute; left: 28px; top: 290px; width: 150px; height: 18px; background: var(--red); color: var(--white); font-size: 10px; font-weight: 700; padding: 2px 0 0 22px; }
  .section-rule { position: absolute; left: 28px; top: 307px; width: 300px; height: 2px; background: var(--black); }
  .checklist-title { font-weight: 900; font-size: 10.5px; text-transform: uppercase; color: var(--black); margin-bottom: 5px; }
  .checklist { list-style: none; font-style: italic; font-weight: 700; font-size: 10px; line-height: 1.6; color: var(--ink); }
  .outdoor { position: absolute; left: 34px; top: 318px; }
  .outdoor .checklist { padding-left: 22px; }
  .member-badge { position: absolute; left: 335px; top: 400px; width: 110px; height: 32px; border: 2px solid #1e3f8f; border-radius: 4px; background: #dfe6f5; }

  /* Inner right */
  .inspections { position: absolute; left: 26px; top: 26px; width: 460px; }
  .inspections .checklist { padding-left: 26px; margin-bottom: 14px; }
  .rooms { margin-top: 6px; }
  .rooms .room-title { color: var(--red); font-weight: 900; font-size: 10px; }
  .rooms .body-copy { padding-left: 26px; margin-bottom: 3px; }
  .callout { position: absolute; left: 40px; top: 398px; width: 440px; color: var(--red); font-weight: 900; font-style: italic; font-size: 14.5px; line-height: 1.3; z-index: 2; }
</style>
</head>
<body>

<section class="spread spread--outer">
  <article class="page page--back">
    <svg class="page-art" viewBox="0 0 510 560">
      <defs>
        <linearGradient id="landscapeFade" x1="0" y1="0" x2="0" y2="1">
          <stop offset="0" stop-color="#ffffff"/>
          <stop offset=".35" stop-color="#cfd8d4"/>
          <stop offset="1" stop-color="#8fa58c"/>
        </linearGradient>
        <linearGradient id="familyTone" x1="0" y1="0" x2="1" y2="1">
          <stop offset="0" stop-color="#c9d3d9"/>
          <stop offset="1" stop-color="#8a7a6c"/>
        </linearGradient>
      </defs>
      <rect role="img" aria-label="Faded coastal landscape photo behind the about text" x="0" y="150" width="510" height="300" fill="url(#landscapeFade)" opacity=".55"/>
      <path d="M0 390 C120 380 260 420 510 350 L510 560 L0 560 Z" fill="var(--red)"/>
      <circle cx="240" cy="352" r="78" fill="var(--red)"/>
      <circle cx="240" cy="352" r="73" fill="var(--white)"/>
      <circle role="img" aria-label="Photo of the founding family smiling on a beach" cx="240" cy="352" r="69" fill="url(#familyTone)"/>
    </svg>
    <div class="about">
      <h2 class="heading">What do we do?</h2>
      <p class="body-copy">We save your time. We perform visual inspections and provide our presence while you are away so you can enjoy your time and home while you are on the island. We have your back!</p>
      <h2 class="heading">Who We Are ?</h2>
      <p class="subhead">We are a family run and operated business.</p>
      <p class="body-copy">Lena is a licensed real estate broker in Hawaii. She has ten years of work experience at a global commercial real estate company. She loves to work with people and find solutions that add value. She holds a Bachelor of Science degree and a Master's degree in Global Leadership.</p>
      <p class="body-copy">Tomas owns a handyman and landscaping firm built on two simple principles: attention to detail and honest work. His ethical and professional approach is unmatched.</p>
      <p class="body-copy">We put our hearts into what we do, guided by care, integrity, respect for the island and sustainable practices whenever possible.</p>
    </div>
    <div class="contact">
      <div>Breeze Keep Care LLC</div>
      <div class="line"><svg viewBox="0 0 12 12"><path d="M3 1 L5 3.5 L4 5 C5 7 6 8 7.5 8.5 L9 7.5 L11 9.5 L9.5 11 C5 10.5 1.5 7 1 2.5 Z" fill="#fff"/></svg>808-555-0142</div>
      <div class="line"><svg viewBox="0 0 12 12"><rect x="1" y="3" width="10" height="7" fill="#fff"/><path d="M1 3 L6 7 L11 3" stroke="var(--red)" fill="none"/></svg>hello@breezekeepcare.com</div>
      <div class="line"><svg viewBox="0 0 12 12"><circle cx="6" cy="6" r="5" fill="#fff"/></svg>www.breezekeepcare.com</div>
    </div>
  </article>

  <article class="page page--front">
    <svg class="page-art" viewBox="0 0 510 560">
      <defs>
        <linearGradient id="villaTone" x1="0" y1="0" x2="0" y2="1">
          <stop offset="0" stop-color="var(--sky)"/>
          <stop offset=".5" stop-color="#d9d4cc"/>
          <stop offset="1" stop-color="var(--sea)"/>
        </linearGradient>
      </defs>
      <path role="img" aria-label="Photo of a tropical villa with a pool and palm trees" d="M0 0 H510 V250 C380 300 220 330 0 320 Z" fill="url(#villaTone)"/>
      <path d="M0 320 C220 330 380 300 510 250 V560 H0 Z" fill="var(--red)"/>
      <path d="M0 390 C180 375 340 320 510 270 V560 H0 Z" fill="var(--white)"/>
      <path d="M0 400 C180 385 340 330 510 280 V560 H0 Z" fill="var(--black)"/>
    </svg>
    <div class="brand-badge">
      <div class="brand-name">Breeze<br>Keep Care</div>
      <div class="brand-tag">Your Home Watch Company</div>
    </div>
    <div class="cover-title">
      <div class="lead">Providing</div>
      <div class="main">Premiere Home Watch &amp;<br>Concierge Services</div>
    </div>
  </article>
</section>

<section class="spread spread--inner">
  <article class="page page--inside-left">
    <svg class="page-art" viewBox="0 0 510 560">
      <defs>
        <linearGradient id="poolTone" x1="0" y1="0" x2="0" y2="1">
          <stop offset="0" stop-color="#9cc7e6"/>
          <stop offset=".55" stop-color="#5f9a5a"/>
          <stop offset="1" stop-color="#2a9ed1"/>
        </linearGradient>
      </defs>
      <path d="M0 520 C180 470 360 480 510 500 V560 H0 Z" fill="var(--black)"/>
      <path d="M0 505 C180 460 360 470 510 490 V500 C360 482 180 475 0 520 Z" fill="var(--red)"/>
      <circle cx="115" cy="480" r="62" fill="var(--red)"/>
      <circle role="img" aria-label="Photo of a screened pool at a home" cx="115" cy="480" r="56" fill="url(#poolTone)"/>
    </svg>
    <div class="intro">
      <h2 class="heading">What is a Home Watch?</h2>
      <p class="body-copy">Home watch is a visual inspection of a vacant home or a vacation rental property where we look for obvious issues and report our findings to you, the client. We can also coordinate maintenance and repair services as well as provide a wide range of concierge services.</p>
    </div>
    <svg class="illustration" role="img" aria-label="Cutaway illustration of a house with inspection icons around it" viewBox="0 0 300 180">
      <defs>
        <radialGradient id="illustrationTone" cx=".5" cy=".5" r=".6">
          <stop offset="0" stop-color="#d4d4d4"/>
          <stop offset="1" stop-color="#f4f4f4"/>
        </radialGradient>
      </defs>
      <rect x="0" y="0" width="300" height="180" fill="url(#illustrationTone)"/>
    </svg>
    <div class="section-tab">Primary Home Watch</div>
    <div class="section-rule"></div>
    <div class="outdoor">
      <h3 class="checklist-title">General Outdoor Visual Inspections</h3>
      <ul class="checklist">
        <li>check yard, lawn &amp; landscaping</li>
        <li>check lanai, deck &amp; pool area for any damage</li>
        <li>check for mold or fading of all outdoor furniture</li>
        <li>check water level of swimming pool or hot tub, if applicable</li>
      </ul>
    </div>
    <div class="member-badge" role="img" aria-label="Accredited member badge"></div>
  </article>

  <article class="page page--inside-right">
    <svg class="page-art" viewBox="0 0 510 560">
      <defs>
        <linearGradient id="beachTone" x1="0" y1="0" x2="0" y2="1">
          <stop offset="0" stop-color="#bfe3f5"/>
          <stop offset=".5" stop-color="#3fb6c9"/>
          <stop offset="1" stop-color="var(--sand)"/>
        </linearGradient>
      </defs>
      <path role="img" aria-label="Photo of a tropical beach with turquoise water" d="M0 400 C200 410 380 390 510 370 V495 C360 480 180 480 0 520 Z" fill="url(#beachTone)"/>
      <path d="M0 520 C180 480 360 480 510 495 V560 H0 Z" fill="var(--black)"/>
      <path d="M0 512 C180 472 360 472 510 487 V495 C360 480 180 480 0 520 Z" fill="var(--white)"/>
    </svg>
    <div class="inspections">
      <h3 class="checklist-title">Home Exterior Visual Inspections</h3>
      <ul class="checklist">
        <li>check security cameras</li>
        <li>check overall damage</li>
        <li>remove mail, newspapers and flyers from mailbox and store inside of the property</li>
        <li>check outdoor plumbing and hoses for leakage</li>
        <li>check garage</li>
        <li>check for vandalism and theft</li>
      </ul>
      <h3 class="checklist-title">Home Interior Visual Inspections</h3>
      <ul class="checklist">
        <li>make sure security system is in working order</li>
        <li>ensure that all doors, windows and sliders are locked and secured</li>
        <li>check thermostats and make sure the air conditioning is set at appropriate and requested temperature</li>
        <li>make sure all smoke detectors are in proper working order or replace batteries if necessary</li>
        <li>visually inspect the water heater and washer and dryer</li>
      </ul>
      <div class="rooms">
        <div class="room-title">Kitchen -</div>
        <p class="body-copy">check under the sink for moisture; make sure refrigerator, freezer, and dishwasher are in working order; run faucets and garbage disposal</p>
        <div class="room-title">Bathrooms -</div>
        <p class="body-copy">check under the sink for moisture; check for leaks and moisture in showers and bathtub; flush toilets and check for leaks; run all the faucets.</p>
        <div class="room-title">Common Interior Inspection -</div>
        <p class="body-copy">water indoor/outdoor plants; check for mold and mildew; check for termites, insects, pests and water intrusion throughout the home.</p>
      </div>
    </div>
    <p class="callout">Don't let repairs or unexpected surprises upon your arrival take away from your vacation time. Arrive knowing all you need to do in Hawaii is relax and enjoy your second home and the island.</p>
  </article>
</section>

</body>
</html>
```